Accounting business needs business card

I have a business card but need something better. I want the colour changed and the design to be better. I have uploaded a picture of my new sign that is grey in colour, i would like to incorporate these colours.

```html
<!DOCTYPE html>
<html lang="en">
<head>
<meta charset="utf-8">
<title>Tally Box – Business Card</title>
<link rel="stylesheet" href="https://fonts.googleapis.com/css2?family=Quicksand:wght@600&family=Ubuntu:wght@400;500&family=Montserrat:wght@500&display=swap">
<style>
  :root {
    --stage: #07121a;
    --paper: #dcdcdc;
    --navy: #0d2249;
    --accent: #1ba8e0;
    --ink: #222326;
    --ink-soft: #3d3f44;
    --white: #f2f2f2;
    --badge-blue: #0a4a93;
    --badge-cyan: #13b5ea;
    --badge-pale: #e9ece4;
  }
  * { margin: 0; padding: 0; box-sizing: border-box; }
  html, body { width: 1200px; height: 1200px; overflow: hidden; }
  body { background: var(--stage); position: relative; font-family: "Ubuntu", sans-serif; }

  .card { position: absolute; left: 221px; width: 758px; height: 434px; overflow: hidden; background: var(--paper); }
  .card--front { top: 117px; }
  .card--back { top: 649px; }
  .card__art { position: absolute; inset: 0; width: 100%; height: 100%; }

  /* Front */
  .contact { position: absolute; left: 461px; top: 34px; list-style: none; }
  .contact__item { display: flex; align-items: center; height: 30px; margin-bottom: 17px; color: var(--white); font-size: 22px; white-space: nowrap; }
  .contact__icon { width: 30px; height: 30px; margin-right: 12px; flex: none; }

  .identity { position: absolute; left: 8px; top: 206px; }
  .identity__name { font-family: "Quicksand", sans-serif; font-weight: 600; font-size: 42px; color: var(--ink); letter-spacing: 0.5px; line-height: 1; white-space: nowrap; }
  .identity__credentials { margin-top: 8px; font-size: 15px; color: var(--ink-soft); }
  .identity__role { margin-top: 5px; font-size: 19px; font-weight: 500; color: var(--ink-soft); letter-spacing: 0.3px; white-space: nowrap; }

  .badges { position: absolute; left: 9px; top: 368px; width: 320px; height: 60px; }

  /* Back */
  .brand { position: absolute; left: 0; width: 423px; top: 0; height: 100%; }
  .brand__mark { position: absolute; left: 143px; top: 126px; width: 126px; height: 126px; }
  .brand__name { position: absolute; left: 0; width: 423px; top: 268px; text-align: center; font-family: "Montserrat", sans-serif; font-weight: 500; font-size: 34px; letter-spacing: 10px; color: var(--ink); padding-left: 10px; white-space: nowrap; }

  .social { position: absolute; left: 456px; top: 204px; display: flex; gap: 16px; list-style: none; }
  .social__item { display: flex; align-items: center; gap: 6px; color: var(--white); font-size: 15px; white-space: nowrap; }
  .social__dot { width: 22px; height: 22px; border-radius: 50%; border: 2px solid var(--accent); }

  .vertical-url { position: absolute; left: 743px; top: 217px; transform: translate(-50%, -50%) rotate(-90deg); color: var(--white); font-size: 15px; white-space: nowrap; }
</style>
</head>
<body>

<section class="card card--front">
  <svg class="card__art" viewBox="0 0 758 434" aria-hidden="true">
    <defs><clipPath id="front-clip"><rect width="758" height="434"/></clipPath></defs>
    <polygon points="187,0 758,0 758,434 431,434" fill="var(--navy)"/>
    <line x1="182" y1="0" x2="426" y2="434" stroke="var(--accent)" stroke-width="5"/>
    <circle cx="621" cy="363" r="136" fill="none" stroke="var(--paper)" stroke-width="8" clip-path="url(#front-clip)"/>
  </svg>

  <ul class="contact">
    <li class="contact__item">
      <svg class="contact__icon" viewBox="0 0 30 30" aria-hidden="true">
        <rect x="1" y="1" width="28" height="28" fill="none" stroke="var(--accent)" stroke-width="1.5"/>
        <path d="M10 6c-2 1-3 3-2 6 2 5 5 9 10 11 2 1 4 0 5-2l-3-3-2 1c-2-1-4-3-5-5l1-2-3-4z" fill="var(--accent)"/>
      </svg>
      0400 555 018
    </li>
    <li class="contact__item">
      <svg class="contact__icon" viewBox="0 0 30 30" aria-hidden="true">
        <rect x="1" y="1" width="28" height="28" fill="none" stroke="var(--accent)" stroke-width="1.5"/>
        <rect x="5" y="8" width="20" height="14" fill="none" stroke="var(--accent)" stroke-width="1.5"/>
        <path d="M5 8l10 8 10-8M5 22l7-7M25 22l-7-7" fill="none" stroke="var(--accent)" stroke-width="1.3"/>
      </svg>
      daniel@tallybox.com.au
    </li>
    <li class="contact__item">
      <svg class="contact__icon" viewBox="0 0 30 30" aria-hidden="true">
        <rect x="1" y="1" width="28" height="28" fill="none" stroke="var(--accent)" stroke-width="1.5"/>
        <circle cx="15" cy="15" r="9" fill="none" stroke="var(--accent)" stroke-width="1.5"/>
        <path d="M9 12c3 0 4 2 6 1s2 3 0 4-1 4 1 5M17 7c1 2 4 2 5 4" fill="none" stroke="var(--accent)" stroke-width="1.5"/>
      </svg>
      www.tallybox.com.au
    </li>
  </ul>

  <div class="identity">
    <h1 class="identity__name">Daniel Marsh</h1>
    <p class="identity__credentials">CPA, MTAX, BCOM (Acc &amp; Fin)</p>
    <p class="identity__role">Taxation and Business Accountant</p>
  </div>

  <svg class="badges" viewBox="0 0 320 60" role="img" aria-label="Professional membership, software partner and registered tax agent badges">
    <rect x="0" y="0" width="142" height="59" fill="var(--badge-blue)"/>
    <circle cx="203" cy="30" r="31" fill="var(--badge-cyan)"/>
    <circle cx="286" cy="24" r="23" fill="var(--badge-pale)" stroke="#9aa08f" stroke-width="1"/>
  </svg>
</section>

<section class="card card--back">
  <svg class="card__art" viewBox="0 0 758 434" aria-hidden="true">
    <rect x="434" y="0" width="324" height="434" fill="var(--navy)"/>
    <rect x="423" y="0" width="5" height="434" fill="var(--accent)"/>
  </svg>

  <div class="brand">
    <svg class="brand__mark" viewBox="0 0 126 126" aria-hidden="true">
      <circle cx="63" cy="63" r="60" fill="none" stroke="var(--ink)" stroke-width="3"/>
    </svg>
    <p class="brand__name">TALLY BOX</p>
  </div>

  <ul class="social">
    <li class="social__item"><span class="social__dot"></span>Kinnect</li>
    <li class="social__item"><span class="social__dot"></span>Workweb</li>
    <li class="social__item"><span class="social__dot"></span>Plusly</li>
  </ul>

  <p class="vertical-url">www.tallybox.com.au</p>
</section>

</body>
</html>
```